Trifold - Gentle Horizon Therapy

Marianne Dobbs, Psy.D.Licensed Psychologist

this is for hypnosis and meditation
I like decorative font for my name (conservative decorative)

calming effect is most imortant

Target Market(s)

clients with depression, pain, anxiety - adults and aged

Industry/Entity Type

Conservative

Font styles to use
Serif

Colors
abd037
85cae6
cadf82
34a7d7
ffffff
886aae
6b449b

Requirements
Must have
• I like zen-like calming effects. lime Green, light blues and purple. I like waves and color.
• I like water and light, flowers and plants - bamboo, stacking rocks, ocean, water, lotus flowers
Should not have
• not too much purple
• Mostly green and blue

```html
<!DOCTYPE html>
<html lang="en">
<head>
<meta charset="utf-8">
<title>Trifold – Gentle Horizon Therapy</title>
<link href="https://fonts.googleapis.com/css2?family=Marcellus&family=Parisienne&family=Montserrat:wght@600;700&display=swap" rel="stylesheet">
<style>
:root{
  --lime:#abd037;
  --lime-soft:#cadf82;
  --sky:#85cae6;
  --blue:#34a7d7;
  --navy:#123f78;
  --purple:#6b449b;
  --lavender:#886aae;
  --white:#ffffff;
  --ink:#2c2c3a;
  --stage:#e9ecef;
}
*{box-sizing:border-box;margin:0;padding:0}
html,body{width:800px;height:1200px;overflow:hidden;background:var(--stage)}
body{font-family:"Marcellus",Georgia,serif;color:var(--ink);position:relative}
.spread{position:absolute;left:30px;width:740px;height:560px;display:flex;box-shadow:0 4px 14px rgba(0,0,0,.18);overflow:hidden}
.spread--outside{top:30px}
.spread--inside{top:610px;background:linear-gradient(120deg,#c9ece6 0%,#d9f1ec 45%,#cfeadf 100%)}
.panel{position:relative;width:246.67px;height:100%;overflow:hidden}
.script{font-family:"Parisienne",cursive;font-weight:400}
.credential{font-family:"Parisienne",cursive;font-size:13px}

/* services panel */
.panel--services{background:linear-gradient(180deg,#f4f9ee 0%,#e6f2c8 45%,var(--lime) 100%);padding:26px 20px 0 20px}
.services-art{position:absolute;right:0;top:60px;width:120px;height:330px;background:radial-gradient(ellipse at 70% 50%,rgba(120,200,60,.55),rgba(171,208,55,0) 70%)}
.services-title{position:relative;font-size:16px;margin-bottom:10px}
.services-title b{font-weight:400;color:var(--ink)}
.service{position:relative;margin-bottom:10px}
.service h3{font-size:11px;color:var(--purple);font-weight:400;margin-bottom:2px}
.service p{font-size:8px;line-height:1.3}
.fee{position:relative;font-family:"Montserrat",sans-serif;font-weight:700;font-size:12.5px;line-height:1.25;margin-top:12px}

/* cover-middle panel */
.panel--intro{background:var(--lime)}
.water{position:absolute;left:0;top:0;width:100%;height:330px;background:linear-gradient(180deg,#0d2f66 0%,var(--navy) 45%,#1d5a9a 100%)}
.intro-text{position:absolute;top:60px;left:0;width:100%;text-align:center;color:var(--white)}
.intro-text .name{font-size:30px;line-height:1}
.intro-text .credential{display:block;text-align:right;padding-right:38px;margin-bottom:-4px}
.intro-text .role{font-size:11px;letter-spacing:.5px;margin-bottom:22px}
.intro-text .motto{font-size:15px;line-height:1.3}
.location{position:absolute;top:398px;left:30px;right:20px;font-size:9px}
.location h4{font-family:"Montserrat",sans-serif;font-size:11px;font-weight:700;margin-bottom:10px}
.location li{list-style:none;display:flex;gap:7px;margin-bottom:7px;line-height:1.3}
.location svg{flex:none;margin-top:1px}

/* cover panel */
.panel--cover{background:var(--lime)}
.lotus-photo{position:absolute;top:0;left:0;width:100%;height:200px;background:radial-gradient(circle at 50% 38%,#8a6fd6 0%,#6b55c4 14%,#4f7a3a 30%,#2f5a2c 70%,#264a22 100%)}
.cover-text{position:absolute;top:205px;left:0;width:100%;text-align:center;color:var(--white)}
.cover-text .credential{display:block;text-align:right;padding-right:40px;margin-bottom:-4px}
.cover-text .name{font-size:28px;line-height:1}
.cover-text .tag{font-size:12px;line-height:1.2}
.cover-text .unleash{font-size:11px;margin-top:12px;line-height:1.2}
.cover-text .unleash small{font-size:9px;display:block}
.special{position:absolute;top:420px;width:100%;text-align:center}
.special h2{font-family:"Montserrat",sans-serif;font-weight:700;font-size:15px;letter-spacing:.5px}
.special p{font-size:9px}
.phone-pill{display:inline-flex;align-items:center;gap:6px;margin-top:6px;background:var(--purple);color:var(--white);font-family:"Montserrat",sans-serif;font-weight:700;font-size:13px;padding:4px 16px;border-radius:14px;border:2px solid var(--white)}
.waves{position:absolute;left:246.67px;top:0;width:493.33px;height:560px;pointer-events:none}

/* inside */
.inside-art{position:absolute;left:30px;top:250px;width:200px;height:180px;background:radial-gradient(circle,rgba(255,255,255,.7) 0%,rgba(255,255,255,0) 70%)}
.inside-panel{padding:34px 20px 0 22px;font-size:8.3px;line-height:1.32}
.inside-panel h2{font-size:14px;font-weight:400;line-height:1.15;margin-bottom:8px}
.inside-panel h2 em{font-style:normal;color:var(--purple)}
.inside-panel h3{font-size:12px;font-weight:400;color:var(--purple);margin:8px 0 6px;line-height:1.2}
.inside-panel p{position:relative;margin-bottom:6px}
.tick-list{list-style:none;position:relative}
.tick-list li{display:flex;gap:6px;align-items:flex-start;font-family:"Montserrat",sans-serif;font-weight:600;font-size:9px;margin-bottom:3px;line-height:1.2}
.tick-list.small li{font-family:"Marcellus",serif;font-weight:400;font-size:8.3px}
.tick-list svg{flex:none;margin-top:1px}
.portrait{width:100px;height:100px;border-radius:50%;border:4px solid var(--lime);margin:0 auto 8px;background:linear-gradient(160deg,#f3f1ec,#d9c9b3 60%,#bfe3de)}
.bio-name{text-align:center;margin-bottom:8px}
.bio-name .credential{display:block;text-align:right;padding-right:30px;margin-bottom:-6px}
.bio-name .name{font-size:28px;line-height:1}
.stripe{position:absolute;left:0;bottom:0;width:100%;height:6px;background:var(--lavender)}
</style>
</head>
<body>

<section class="spread spread--outside" aria-label="Brochure outside">
  <article class="panel panel--services">
    <div class="services-art" role="img" aria-label="Soft green bamboo leaves"></div>
    <h2 class="services-title">Psychological <b>Services</b></h2>
    <div class="service"><h3>Initial evaluation</h3><p>Mental health assessment, diagnosis and comprehensive wellness planning.</p></div>
    <div class="service"><h3>Gentle Horizon Therapy (GHT)</h3><p>Resolve emotional distress, heartbreak and grief. GHT clears trauma at the subconscious level with hypnotic communication. The most troubling of memories are worked through and clients gain a sense of clarity, peace and power. Only a couple of sessions are needed to experience dramatic and long-lasting effects.</p></div>
    <div class="service"><h3>Eye Movement Desensitization and Reprocessing (EMDR)</h3><p>Evidence-based treatment for post-traumatic stress disorder, anxiety, depression and adverse experiences. Experience relief and empowerment. More information at emdrguide.org.</p></div>
    <div class="service"><h3>Short-term talk therapy</h3><p>Psychotherapy to create a more satisfying life. Proactive approach to seeking effective solutions for your most pressing emotional and relational problems.</p></div>
    <div class="service"><h3>Meditation for Wellness</h3><p>Personalized meditation for calm, healing and well-being.</p></div>
    <p class="fee">FEE INFORMATION: ELDERCARE PLUS AND SERVICECARE ACCEPTED AND FILED.</p>
  </article>

  <article class="panel panel--intro">
    <div class="water" role="img" aria-label="Calm deep blue ocean water"></div>
    <div class="intro-text">
      <span class="credential">Psy.D.</span>
      <div class="name script">Marianne Dobbs</div>
      <p class="role">LICENSED PSYCHOLOGIST</p>
      <p class="motto">Heal the Past<br>Embrace the Present<br>Create the Future</p>
    </div>
    <div class="location">
      <h4>Office Location:</h4>
      <ul>
        <li><svg width="9" height="11" viewBox="0 0 9 11"><path d="M4.5 0A4 4 0 0 0 .5 4c0 3 4 7 4 7s4-4 4-7a4 4 0 0 0-4-4z" fill="var(--purple)"/><circle cx="4.5" cy="4" r="1.5" fill="var(--lime)"/></svg><span>Harbor Point Plaza<br>480 Shoreline Dr #12<br>Seabreeze, FL 30001</span></li>
        <li><svg width="10" height="10" viewBox="0 0 10 10"><circle cx="5" cy="5" r="4.4" fill="none" stroke="var(--purple)"/><path d="M3.3 2.8l1 .9-.5.8c.4.8.9 1.3 1.7 1.7l.8-.5.9 1-.8.8C4.5 7.2 2.8 5.5 2.5 3.6z" fill="var(--purple)"/></svg><span>555 014-2093</span></li>
        <li><svg width="10" height="10" viewBox="0 0 10 10"><circle cx="5" cy="5" r="4.4" fill="none" stroke="var(--purple)"/><path d="M.6 5h8.8M5 .6c-2 2.5-2 6.3 0 8.8M5 .6c2 2.5 2 6.3 0 8.8" fill="none" stroke="var(--purple)" stroke-width=".7"/></svg><span>www.gentlehorizonwellness.com</span></li>
      </ul>
    </div>
  </article>

  <article class="panel panel--cover">
    <div class="lotus-photo" role="img" aria-label="Purple lotus flower on green lily pads"></div>
    <div class="cover-text">
      <span class="credential">Psy.D.</span>
      <div class="name script">Marianne Dobbs</div>
      <p class="tag">Live Well, Love Well</p>
      <p class="tag">LICENSED PSYCHOLOGIST</p>
      <p class="unleash">Unleashing the Power<small>of the Mind for Healing and Well-being</small></p>
    </div>
    <div class="special">
      <h2>SPECIALIZING IN</h2>
      <p>Adults and Gentle Horizon Therapy</p>
      <span class="phone-pill"><svg width="12" height="12" viewBox="0 0 10 10"><circle cx="5" cy="5" r="4.4" fill="none" stroke="#fff"/><path d="M3.3 2.8l1 .9-.5.8c.4.8.9 1.3 1.7 1.7l.8-.5.9 1-.8.8C4.5 7.2 2.8 5.5 2.5 3.6z" fill="#fff"/></svg>555 014-2093</span>
    </div>
  </article>

  <svg class="waves" viewBox="0 0 493.33 560" preserveAspectRatio="none" aria-hidden="true">
    <path d="M0 330 C80 318 160 340 246.67 322 L246.67 338 C160 354 80 336 0 346Z" fill="var(--sky)"/>
    <path d="M0 346 C80 336 160 354 246.67 338 L246.67 352 C160 366 80 350 0 358Z" fill="var(--blue)"/>
    <path d="M246.67 215 C320 175 400 205 493.33 180 L493.33 200 C400 222 320 192 246.67 232Z" fill="var(--white)"/>
    <path d="M246.67 232 C320 192 400 222 493.33 200 L493.33 214 C400 236 320 208 246.67 246Z" fill="var(--sky)"/>
    <path d="M246.67 246 C320 208 400 236 493.33 214 L493.33 372 C400 390 320 378 246.67 396Z" fill="var(--purple)"/>
    <path d="M246.67 396 C320 378 400 390 493.33 372 L493.33 384 C400 402 320 392 246.67 408Z" fill="var(--white)"/>
    <path d="M246.67 408 C320 392 400 402 493.33 384 L493.33 390 C400 408 320 398 246.67 414Z" fill="var(--blue)"/>
  </svg>
</section>

<section class="spread spread--inside" aria-label="Brochure inside">
  <div class="inside-art" role="img" aria-label="Faint white dandelion seed head"></div>

  <article class="panel inside-panel">
    <h2>What is <em>Gentle Horizon Therapy (GHT)</em></h2>
    <p>GHT dramatically enhances mood, creates calm, eases grief, optimizes health and promotes success. It is a form of hypnosis that clears stuck patterns of thinking and feeling at the subconscious level. Past emotionally charged memories are cleared. You do not have to talk about problems, share scattered thoughts, cry or re-experience uncomfortable emotions. You are guided to engage in deep brain processing to create an internal shift for automatic changes in thoughts, feelings and behaviors. Profound change happens within your nervous system facilitating lasting positive effects. Only one or two sessions are needed to experience immediate symptom relief.</p>
    <h3>GHT is effective for many of life's problems including:</h3>
    <ul class="tick-list">
      <li><svg width="9" height="9" viewBox="0 0 9 9"><path d="M1 5l2.3 2.3L8 1.5" fill="none" stroke="var(--purple)" stroke-width="1.4"/></svg>PTSD, Sexual Abuse and Childhood Abuse</li>
      <li><svg width="9" height="9" viewBox="0 0 9 9"><path d="M1 5l2.3 2.3L8 1.5" fill="none" stroke="var(--purple)" stroke-width="1.4"/></svg>Grief, Infidelity and Heartbreak</li>
      <li><svg width="9" height="9" viewBox="0 0 9 9"><path d="M1 5l2.3 2.3L8 1.5" fill="none" stroke="var(--purple)" stroke-width="1.4"/></svg>Relationship issues</li>
      <li><svg width="9" height="9" viewBox="0 0 9 9"><path d="M1 5l2.3 2.3L8 1.5" fill="none" stroke="var(--purple)" stroke-width="1.4"/></svg>Anger and Resentment</li>
      <li><svg width="9" height="9" viewBox="0 0 9 9"><path d="M1 5l2.3 2.3L8 1.5" fill="none" stroke="var(--purple)" stroke-width="1.4"/></svg>Guilt / Shame</li>
      <li><svg width="9" height="9" viewBox="0 0 9 9"><path d="M1 5l2.3 2.3L8 1.5" fill="none" stroke="var(--purple)" stroke-width="1.4"/></svg>Anxiety / Fear</li>
      <li><svg width="9" height="9" viewBox="0 0 9 9"><path d="M1 5l2.3 2.3L8 1.5" fill="none" stroke="var(--purple)" stroke-width="1.4"/></svg>Nightmares / Insomnia</li>
      <li><svg width="9" height="9" viewBox="0 0 9 9"><path d="M1 5l2.3 2.3L8 1.5" fill="none" stroke="var(--purple)" stroke-width="1.4"/></svg>Stress-related symptoms and Pain</li>
    </ul>
  </article>

  <article class="panel inside-panel">
    <h2>CLEARING OLD STUFF AND MAKING WAY FOR <em>NEW BEGINNINGS</em></h2>
    <p>If you have been unable to change how you feel, think or act, it is likely that you are being affected by experiences from your past. When something is painful or disturbing, it slams into awareness and leaves a lasting impression. Even when the experience is finished, deeper parts of the mind may continue to respond as if the disturbing event is still occurring. When fueled by the ongoing influence of past events, emotional problems and destructive behaviors feel impossible to overcome. You may consciously understand the value of changing a behavior, but unless your deeper mind is transformed, change is not likely. In GHT the subconscious mind is engaged, and the influence of past events is eliminated. Energy that was blocked is released and healing takes place. Negative habits and painful emotions are replaced by feelings of well-being and motivation for desired action.</p>
    <h3>What happens in a GHT Session?</h3>
    <p>Trauma is stored in the mind and body. In GHT, you will experience profound physiological calm and you will be guided towards emotional resolution in a gentle, creative and even humorous way. You access inner resources of light, wisdom and peace. You step into the awareness of your true and safe self. As Paul Avery states, "we all have a beautiful light within; we just sometimes forget it is there." From this place of light, emotional memories are easily reframed with new meaning. You will leave the session feeling peaceful and sourced from within by a free-flowing energy.</p>
    <h3>Clear Your Mind and Change Your World</h3>
    <ul class="tick-list small">
      <li><svg width="9" height="9" viewBox="0 0 9 9"><path d="M1 5l2.3 2.3L8 1.5" fill="none" stroke="var(--purple)" stroke-width="1.4"/></svg>Discover and resolve subconscious causes for emotional and behavioral difficulties</li>
      <li><svg width="9" height="9" viewBox="0 0 9 9"><path d="M1 5l2.3 2.3L8 1.5" fill="none" stroke="var(--purple)" stroke-width="1.4"/></svg>Eliminate unconscious conflicts blocking desired change</li>
      <li><svg width="9" height="9" viewBox="0 0 9 9"><path d="M1 5l2.3 2.3L8 1.5" fill="none" stroke="var(--purple)" stroke-width="1.4"/></svg>Promote mind / body healing</li>
    </ul>
  </article>

  <article class="panel inside-panel">
    <div class="portrait" role="img" aria-label="Portrait photo of the psychologist"></div>
    <div class="bio-name"><span class="credential">Psy.D.</span><span class="name script">Dr. Marianne Dobbs</span></div>
    <p>Dr. Dobbs is a licensed clinical psychologist specializing in adults and seniors.</p>
    <p>She treats people for depression, anxiety, grief, sexual trauma, PTSD, relationship issues, infidelity, divorce and stress-related symptoms.</p>
    <p>She has over 20 years of clinical experience in mental health and is an adjunct counseling professor at Westbrook University.</p>
    <p>She received her Master's and Doctorate degrees in Clinical Psychology from Harbor Institute, Pacific Coast College in Honolulu, Hawaii.</p>
    <p>She earned a Bachelor's of Science degree in Rehabilitation Medicine from Lakeshore University in Ontario, Canada. At Seaside Holistic Wellness Center, she provides initial evaluations, assessment, diagnosis and comprehensive treatment planning.</p>
    <p>She will collaborate with you to create solutions for healing, empowerment and wellness.</p>
  </article>

  <div class="stripe"></div>
</section>

</body>
</html>
```